Business card & Stationary (e.g. Letterhead, Folder design, etc) for Financial Education Company
MoneyPathways
Creative Brief
Simple
Calder Pruitt
Founder & CEO
42 Hadley Ct, Closter, NJ 07624
calder@moneypathways.org
moneypathways.org
I would like to see a nice design, but I am leaving it up to you. It could be the company logo or name but with a nice design.

```html
<!DOCTYPE html>
<html lang="en">
<head>
<meta charset="utf-8">
<title>MoneyPathways — Business Card</title>
<link rel="stylesheet" href="https://fonts.googleapis.com/css2?family=Montserrat:wght@400;500;600;800&display=swap">
<style>
  :root {
    --bg: #1a1b1e;
    --card-dark: #242529;
    --paper: #ffffff;
    --teal: #4fb3a9;
    --green: #2f7d3a;
    --green-light: #6cbf4a;
    --ink: #2b2d31;
    --white: #ffffff;
    --faint: rgba(79, 179, 169, 0.16);
  }
  * { margin: 0; padding: 0; box-sizing: border-box; }
  html, body {
    width: 1200px; height: 963px; overflow: hidden;
    background: var(--bg);
    font-family: "Montserrat", sans-serif;
  }
  .stage {
    position: relative; width: 1200px; height: 963px;
    display: flex; flex-direction: column; align-items: center; justify-content: center; gap: 44px;
  }
  .card {
    position: relative; width: 600px; height: 343px;
    border-radius: 18px; overflow: hidden;
    box-shadow: 0 14px 40px rgba(0,0,0,0.45);
  }

  /* Front */
  .card-front { background: var(--paper); }
  .front-brand {
    position: absolute; left: 0; right: 0; top: 0; height: 178px;
    display: flex; align-items: center; justify-content: center; gap: 16px;
  }
  .brand-dot { width: 56px; height: 56px; border-radius: 50%; background: var(--teal); flex: none; }
  .brand-name { font-weight: 800; font-size: 38px; color: var(--ink); letter-spacing: -0.5px; white-space: nowrap; }
  .front-stripes { position: absolute; left: 0; right: 0; top: 178px; }
  .stripe-dark { height: 5px; background: var(--green); }
  .stripe-gap { height: 3px; background: var(--paper); }
  .stripe-light { height: 3px; background: var(--green-light); }
  .front-info {
    position: absolute; left: 0; right: 0; top: 189px; bottom: 0;
    background: var(--teal);
    display: flex; align-items: center; justify-content: center;
    color: var(--white);
  }
  .info-person { text-align: right; padding-right: 26px; white-space: nowrap; }
  .person-name { font-weight: 600; font-size: 19px; }
  .person-title { font-size: 13px; font-weight: 500; margin-top: 4px; }
  .person-address { font-size: 13px; font-weight: 400; margin-top: 16px; }
  .info-divider { width: 1px; height: 96px; background: rgba(255,255,255,0.75); flex: none; }
  .info-contact { list-style: none; padding-left: 26px; font-size: 13px; font-weight: 400; white-space: nowrap; }
  .info-contact li { display: flex; align-items: center; gap: 9px; line-height: 26px; }
  .info-contact svg { width: 13px; height: 13px; flex: none; }

  /* Back */
  .card-back { background: var(--card-dark); }
  .back-mark {
    position: absolute; left: -70px; top: 40px; width: 230px; height: 230px;
    border-radius: 50%; border: 32px solid var(--faint);
  }
  .back-name {
    position: absolute; right: 54px; top: 152px;
    font-weight: 800; font-size: 40px; color: var(--white); letter-spacing: -0.5px; white-space: nowrap;
  }
</style>
</head>
<body>
<main class="stage">
  <section class="card card-front" aria-label="Business card front">
    <div class="front-brand">
      <span class="brand-dot"></span>
      <span class="brand-name">MoneyPathways</span>
    </div>
    <div class="front-stripes">
      <div class="stripe-dark"></div>
      <div class="stripe-gap"></div>
      <div class="stripe-light"></div>
    </div>
    <div class="front-info">
      <div class="info-person">
        <p class="person-name">Calder Pruitt</p>
        <p class="person-title">Founder &amp; CEO</p>
        <p class="person-address">42 Hadley Ct, Brookvale, NJ 07555</p>
      </div>
      <div class="info-divider"></div>
      <ul class="info-contact">
        <li>
          <svg viewBox="0 0 16 16" fill="none" stroke="#fff" stroke-width="1.6" stroke-linecap="round" stroke-linejoin="round"><path d="M3 2h3l1.5 3.5-2 1.2a8 8 0 0 0 3.8 3.8l1.2-2L14 10v3a1.5 1.5 0 0 1-1.5 1.5A11.5 11.5 0 0 1 1.5 3.5 1.5 1.5 0 0 1 3 2z"/></svg>
          555-014-2290
        </li>
        <li>
          <svg viewBox="0 0 16 16" fill="none" stroke="#fff" stroke-width="1.6" stroke-linejoin="round"><rect x="1.5" y="3.5" width="13" height="9" rx="1"/><path d="M1.5 4l6.5 5 6.5-5"/></svg>
          calder@moneypathways.org
        </li>
        <li>
          <svg viewBox="0 0 16 16" fill="none" stroke="#fff" stroke-width="1.4"><circle cx="8" cy="8" r="6.5"/><ellipse cx="8" cy="8" rx="3" ry="6.5"/><path d="M1.5 8h13"/></svg>
          moneypathways.org
        </li>
      </ul>
    </div>
  </section>

  <section class="card card-back" aria-label="Business card back">
    <div class="back-mark"></div>
    <span class="back-name">MoneyPathways</span>
  </section>
</main>
</body>
</html>
```